Creative Brief
Eastmoor Directorate - Bahrain
Business Cards + Stationary materials.
Simple
Tariq Yousef Al-Mansoori
Head of Financial Affairs
P.O. Box 37182, Awali. Kingdom of Bahrain
talmansoori@eastmoor-dir.example
www.eastmoor-dir.example
We would like the design to include the following colors : cyan, golden & silver. But we are open to new ideas that match our new logo.
Stationary items include :
- A4 letterhead ( would prefer the logo in the top middle section so that we can write the office name on either side of the A4 paper. We would like to use the attached watermark image ( you can change the color to match the theme )
- Notepad
- Presentation folder
- Envelopes ( A4, A3, basically the whole nine yards)
a short explanation on the attached files :
* ED Logo : main logo that represents our office (available in B&W and colored)
* Watermark : design we want as a watermark on the stationary
* Horizon : logo (available in different sizes) that should appear close to the address line and should appear on all stationary materials and business cards. This represents Bahrain horizon plan for economic development, more info can be found here : http://www.horizonplan.example/web/ , or http://wiki.example.org/wiki/Bahrain_Horizon_Plan
We would like to also point out that the back side of the business card MUST include the same information as the front but in Arabic language, you can find the translated info below.
Name : طارق يوسف المنصوري
Title : رئيس الموارد المالية
address :
ص.ب 37182، عوالي. مملكة البحرين
all the other info should be the same.
We wouldn't mind seeing different types of fonts as long as they are professional, serious and formal.
ED Logo : main logo that represents our office - in black and white
ED Logo : main logo that represents our office - colored
design we want as a watermark on the stationary
logo that should appear close to the address line and should appear on all stationary materials and business cards. This represents Bahrain horizon plan for economic development, more info can be found here : http://www.horizonplan.example/web/ ,or http://wiki.example.org/wiki/Bahrain_Horizon_Plan

```html
<!DOCTYPE html>
<html lang="en">
<head>
<meta charset="utf-8">
<title>Eastmoor Directorate – Stationery Set</title>
<link rel="stylesheet" href="https://fonts.googleapis.com/css2?family=Lato:wght@400;700&family=Amiri:wght@400;700&display=swap">
<style>
  :root {
    --backdrop: #e7e3dd;
    --paper: #fbfcfd;
    --paper-tint: #eef6fa;
    --paper-warm: #fbf7ea;
    --navy: #213f86;
    --gold: #b9a468;
    --silver: #c5cbd2;
    --ink: #3b4252;
    --ink-soft: #8a93a0;
    --mark-wash: #dfeaf1;
  }
  * { box-sizing: border-box; margin: 0; padding: 0; }
  html, body { width: 1200px; height: 619px; overflow: hidden; }
  body {
    background: var(--backdrop);
    font-family: "Lato", Arial, sans-serif;
    color: var(--ink);
    position: relative;
  }

  /* ---------- shared brand pieces ---------- */
  .brand {
    position: absolute;
    display: flex; align-items: center; gap: 3px;
    font-size: 6px; font-weight: 700; color: var(--navy);
    white-space: nowrap;
  }
  .brand::before {
    content: ""; width: 9px; height: 9px; border-radius: 50%;
    border: 1px solid var(--navy);
  }
  .horizon-mark {
    position: absolute; left: 8px; bottom: 6px;
    font-size: 5px; font-weight: 700; color: var(--gold);
    letter-spacing: .3px;
  }
  .band {
    position: absolute; left: 22%; right: 0; bottom: 6px; height: 3px;
    background: linear-gradient(90deg, var(--navy) 0 82%, var(--gold) 82% 100%);
  }
  .watermark {
    position: absolute; left: 18%; right: 18%;
    border-radius: 50%;
    background: radial-gradient(ellipse at center, var(--mark-wash) 0%, rgba(223,234,241,0) 70%);
  }

  /* ---------- letterheads ---------- */
  .sheet {
    position: absolute; top: 44px; width: 216px; height: 300px;
    background: linear-gradient(160deg, var(--paper) 0%, var(--paper-tint) 100%);
    box-shadow: 0 1px 3px rgba(0,0,0,.18);
  }
  .sheet--plain { background: linear-gradient(160deg, #ffffff 0%, #f1f4f6 100%); }
  .sheet--fax { background: linear-gradient(120deg, var(--paper-tint) 0%, var(--paper-warm) 55%, var(--paper-tint) 100%); }
  .sheet .brand { top: 8px; right: 10px; }
  .sheet .watermark { top: 120px; height: 90px; }
  .sender {
    position: absolute; top: 9px; left: 10px;
    font-size: 3.6px; line-height: 5px; color: var(--ink-soft);
  }

  .fax-title { position: absolute; top: 62px; left: 12px; font-size: 11px; font-weight: 700; color: var(--ink); letter-spacing: .5px; }
  .fax-fields {
    position: absolute; top: 80px; left: 12px; right: 12px;
    display: grid; grid-template-columns: 1fr 1fr; column-gap: 10px; row-gap: 6px;
  }
  .fax-field {
    font-size: 4px; color: var(--ink-soft);
    border-bottom: .6px solid var(--silver); padding-bottom: 1px;
  }
  .fax-checks {
    position: absolute; top: 128px; left: 12px; right: 12px;
    display: flex; justify-content: space-between;
    font-size: 3.6px; color: var(--ink-soft);
  }
  .fax-checks span::before {
    content: ""; display: inline-block; width: 3.5px; height: 3.5px;
    border: .5px solid var(--ink-soft); margin-right: 1.5px; vertical-align: -0.5px;
  }

  /* ---------- envelopes ---------- */
  .envelope {
    position: absolute;
    background: linear-gradient(160deg, var(--paper) 0%, var(--paper-tint) 100%);
    box-shadow: 0 1px 3px rgba(0,0,0,.2);
    overflow: hidden;
  }
  .envelope--warm { background: linear-gradient(150deg, #ffffff 0%, var(--paper-warm) 100%); }
  .envelope .flap { position: absolute; inset: 0; width: 100%; height: 100%; }
  .envelope .brand { left: 50%; transform: translateX(-50%); }
  .envelope--back .brand { top: 8px; }
  .envelope--front .brand { top: 6px; }
  .envelope--front .watermark { top: 34%; height: 40%; }

  /* ---------- business cards ---------- */
  .card {
    position: absolute; left: 1048px; width: 106px; height: 50px;
    background: linear-gradient(150deg, #ffffff 0%, var(--paper-tint) 100%);
    box-shadow: 0 1px 3px rgba(0,0,0,.2);
    overflow: hidden;
  }
  .card .brand { top: 4px; right: 5px; font-size: 4.6px; }
  .card .brand::before { width: 7px; height: 7px; }
  .card-name { position: absolute; top: 17px; left: 6px; font-size: 4.4px; font-weight: 700; color: var(--navy); }
  .card-role { position: absolute; top: 23px; left: 6px; font-size: 3.4px; color: var(--ink-soft); }
  .card-contact { position: absolute; top: 29px; left: 6px; font-size: 3px; line-height: 4px; color: var(--ink-soft); white-space: nowrap; }
  .card .band { bottom: 4px; height: 2.5px; }
  .card--arabic .card-name, .card--arabic .card-role, .card--arabic .card-contact {
    left: auto; right: 6px; text-align: right; direction: rtl;
    font-family: "Amiri", "Times New Roman", serif;
  }
  .card--arabic .card-name { font-size: 5px; top: 15px; }
  .card--arabic .card-role { font-size: 4px; top: 22px; }
  .card--arabic .card-contact { font-size: 3.6px; top: 28px; }
  .card--arabic .brand { right: auto; left: 5px; }
</style>
</head>
<body>

  <!-- Letterhead -->
  <section class="sheet" style="left:48px">
    <div class="sender">Eastmoor Directorate<br>P.O. Box 0000, City<br>www.eastmoor-dir.example</div>
    <div class="brand">Eastmoor Directorate</div>
    <div class="watermark" role="img" aria-label="Faint calligraphic watermark"></div>
    <div class="horizon-mark">Horizon</div>
    <div class="band"></div>
  </section>

  <!-- Letterhead, plain stock -->
  <section class="sheet sheet--plain" style="left:420px">
    <div class="sender">Eastmoor Directorate<br>P.O. Box 0000, City<br>www.eastmoor-dir.example</div>
    <div class="brand">Eastmoor Directorate</div>
    <div class="watermark" role="img" aria-label="Faint calligraphic watermark"></div>
    <div class="horizon-mark">Horizon</div>
    <div class="band"></div>
  </section>

  <!-- Fax sheet -->
  <section class="sheet sheet--fax" style="left:756px">
    <div class="sender">Eastmoor Directorate<br>P.O. Box 0000, City<br>www.eastmoor-dir.example</div>
    <div class="brand">Eastmoor Directorate</div>
    <h1 class="fax-title">FAX</h1>
    <div class="fax-fields">
      <div class="fax-field">To:</div><div class="fax-field">From:</div>
      <div class="fax-field">Fax:</div><div class="fax-field">Phone:</div>
      <div class="fax-field">Date:</div><div class="fax-field">Pages:</div>
      <div class="fax-field">Re:</div><div class="fax-field">CC:</div>
    </div>
    <div class="fax-checks">
      <span>Urgent</span><span>Review</span><span>Comment</span><span>Reply</span><span>Recycle</span>
    </div>
    <div class="watermark" role="img" aria-label="Faint calligraphic watermark"></div>
    <div class="horizon-mark">Horizon</div>
    <div class="band"></div>
  </section>

  <!-- Business cards -->
  <section class="card" style="top:130px">
    <div class="brand">Eastmoor Directorate</div>
    <div class="card-name">Staff Name</div>
    <div class="card-role">Department Title</div>
    <div class="card-contact">P.O. Box 0000, City<br>mail@eastmoor-dir.example</div>
    <div class="band"></div>
  </section>
  <section class="card card--arabic" style="top:226px">
    <div class="brand">Eastmoor Directorate</div>
    <div class="card-name" lang="ar">اسم الموظف</div>
    <div class="card-role" lang="ar">المسمى الوظيفي</div>
    <div class="card-contact" lang="ar">ص.ب 0000، المدينة</div>
    <div class="band"></div>
  </section>

  <!-- Envelope set 1 -->
  <section class="envelope envelope--back" style="left:80px;top:362px;width:290px;height:130px">
    <svg class="flap" viewBox="0 0 290 130" preserveAspectRatio="none" aria-hidden="true">
      <polyline points="0,0 145,60 290,0" fill="none" stroke="#c5cbd2" stroke-width="1"/>
    </svg>
    <div class="brand">Eastmoor Directorate</div>
  </section>
  <section class="envelope envelope--front" style="left:48px;top:430px;width:250px;height:146px">
    <div class="brand">Eastmoor Directorate</div>
    <div class="watermark" role="img" aria-label="Faint calligraphic watermark"></div>
    <div class="horizon-mark">Horizon</div>
    <div class="band"></div>
  </section>

  <!-- Envelope set 2 -->
  <section class="envelope envelope--back" style="left:410px;top:362px;width:296px;height:130px">
    <svg class="flap" viewBox="0 0 296 130" preserveAspectRatio="none" aria-hidden="true">
      <polyline points="0,0 148,60 296,0" fill="none" stroke="#c5cbd2" stroke-width="1"/>
    </svg>
    <div class="brand">Eastmoor Directorate</div>
  </section>
  <section class="envelope envelope--front" style="left:412px;top:450px;width:278px;height:126px">
    <div class="brand">Eastmoor Directorate</div>
    <div class="watermark" role="img" aria-label="Faint calligraphic watermark"></div>
    <div class="horizon-mark">Horizon</div>
    <div class="band"></div>
  </section>

  <!-- Envelope set 3 -->
  <section class="envelope envelope--back envelope--warm" style="left:748px;top:362px;width:334px;height:130px">
    <svg class="flap" viewBox="0 0 334 130" preserveAspectRatio="none" aria-hidden="true">
      <polyline points="0,0 167,60 334,0" fill="none" stroke="#c5cbd2" stroke-width="1"/>
    </svg>
    <div class="brand">Eastmoor Directorate</div>
  </section>
  <section class="envelope envelope--front envelope--warm" style="left:746px;top:450px;width:308px;height:126px">
    <div class="brand">Eastmoor Directorate</div>
    <div class="watermark" role="img" aria-label="Faint calligraphic watermark"></div>
    <div class="horizon-mark">Horizon</div>
    <div class="band"></div>
  </section>

</body>
</html>
```